Business Card

Please design a business card with our logo on a cream coloured background and include the following information:

Tallowmere Shopping Centre
ph (08) 9314 8806

sales@quillmeadowflorist.com

www.quillmeadowflorist.com

on reverse:

Find us on Petalnet
petalnet.com/quillmeadowflorist

```html
<!DOCTYPE html>
<html lang="en">
<head>
<meta charset="utf-8">
<title>Quill Meadow Florist – Business Card</title>
<link rel="stylesheet" href="https://fonts.googleapis.com/css2?family=Fira+Sans:wght@400;500&family=Fira+Sans+Condensed:wght@500&display=swap">
<style>
  :root {
    --page-bg: #ece9e2;
    --green-deep: #3f8a22;
    --green-mid: #5aa82c;
    --green-light: #8cc63f;
    --ink-light: #ffffff;
    --ink-soft: rgba(255,255,255,0.9);
  }
  * { box-sizing: border-box; margin: 0; padding: 0; }
  html, body {
    width: 1200px; height: 480px; overflow: hidden;
    background: var(--page-bg);
    font-family: "Fira Sans", sans-serif;
  }
  .canvas { position: relative; width: 1200px; height: 480px; }
  .card {
    position: absolute; top: 90px;
    width: 520px; height: 300px;
    border-radius: 4px;
    overflow: hidden;
    box-shadow: 0 6px 18px rgba(0,0,0,0.18);
    background: linear-gradient(135deg, var(--green-light) 0%, var(--green-mid) 45%, var(--green-deep) 100%);
  }
  .card--back { left: 60px; }
  .card--front { left: 620px; }
  .card__decor {
    position: absolute; inset: 0;
    background:
      radial-gradient(ellipse 45% 70% at 20% 60%, rgba(160,215,80,0.45), transparent 70%),
      radial-gradient(ellipse 35% 60% at 85% 30%, rgba(160,215,80,0.35), transparent 70%);
  }
  .card--front .card__decor {
    background:
      radial-gradient(ellipse 40% 70% at 15% 40%, rgba(160,215,80,0.45), transparent 70%),
      radial-gradient(ellipse 40% 70% at 90% 55%, rgba(160,215,80,0.4), transparent 70%);
  }
  .social {
    position: absolute; left: 120px; top: 130px;
    color: var(--ink-soft);
    font-size: 16px; line-height: 1.3;
  }
  .brand {
    position: absolute; top: 22px; left: 0; right: 0;
    text-align: center;
  }
  .brand__mark {
    display: block; margin: 0 auto 14px;
    width: 58px; height: 58px; border-radius: 50%;
    background: var(--ink-light);
  }
  .brand__name {
    font-family: "Fira Sans Condensed", sans-serif;
    font-weight: 500; font-size: 33px;
    color: var(--ink-light);
    letter-spacing: 0.2px;
  }
  .contact {
    position: absolute; left: 110px; top: 158px;
    list-style: none;
    color: var(--ink-soft);
    font-size: 12px; line-height: 1.25;
  }
  .contact__item { display: flex; align-items: center; gap: 10px; margin-bottom: 2px; }
  .contact__item--gap { margin-top: 14px; }
  .contact__icon { width: 12px; height: 12px; flex: none; }
  .website {
    position: absolute; left: 0; right: 0; bottom: 30px;
    text-align: center;
    color: var(--ink-soft);
    font-size: 11px; letter-spacing: 3px;
  }
</style>
</head>
<body>
<main class="canvas">
  <section class="card card--back" aria-label="Card reverse">
    <div class="card__decor" role="img" aria-label="Soft green leaf-petal backdrop"></div>
    <p class="social">Find us on Petalnet<br>petalnet.com/quillmeadowflorist</p>
  </section>

  <section class="card card--front" aria-label="Card front">
    <div class="card__decor" role="img" aria-label="Soft green leaf-petal backdrop"></div>
    <header class="brand">
      <span class="brand__mark"></span>
      <h1 class="brand__name">Quill Meadow Florist</h1>
    </header>
    <ul class="contact">
      <li class="contact__item">
        <svg class="contact__icon" viewBox="0 0 12 12"><path d="M6 1a3.5 3.5 0 0 0-3.5 3.5C2.5 7.5 6 11 6 11s3.5-3.5 3.5-6.5A3.5 3.5 0 0 0 6 1zm0 5a1.4 1.4 0 1 1 0-2.8A1.4 1.4 0 0 1 6 6z" fill="#fff"/></svg>
        Tallowmere Shopping Centre
      </li>
      <li class="contact__item">
        <svg class="contact__icon" viewBox="0 0 12 12"><path d="M3 1l2 2.5-1.2 1.3a6 6 0 0 0 3.4 3.4L8.5 7 11 9l-1.2 1.8C5.5 10.8 1.2 6.5 1.2 2.2z" fill="#fff"/></svg>
        phone (08) 9314 8806
      </li>
      <li class="contact__item">
        <svg class="contact__icon" viewBox="0 0 12 12"><circle cx="6" cy="6" r="4.6" fill="none" stroke="#fff" stroke-width="1.2"/><path d="M1.4 6h9.2M6 1.4c-2.4 2.6-2.4 6.6 0 9.2M6 1.4c2.4 2.6 2.4 6.6 0 9.2" fill="none" stroke="#fff" stroke-width="0.9"/></svg>
        www.quillmeadowflorist.com
      </li>
      <li class="contact__item contact__item--gap">
        <svg class="contact__icon" viewBox="0 0 12 12"><rect x="1" y="2.5" width="10" height="7" rx="1" fill="#fff"/><path d="M1.5 3l4.5 3.5L10.5 3" fill="none" stroke="#5aa82c" stroke-width="1"/></svg>
        sales@quillmeadowflorist.com
      </li>
    </ul>
    <p class="website">www.quillmeadowflorist.com</p>
  </section>
</main>
</body>
</html>
```